依頼詳細
妊活専門のサプリメントとして、
妊娠を意識した初期から摂取してもらうサプリメントです。
オーガニックのイメージ
伝統のイメージ
信頼感のイメージ
こちらを意識してご提案お願いいたします。
記載項目
サイズ  w90mm×h 95mm
記載内容 FLORIMAオーガニック葉酸 FLORIMA-LABO
オーガニック天然葉酸+妊活に必須栄養素配合
希望イメージ
シンプル 複雑
単色 カラフル
暗い 明るい
日常 高級
遊び心 厳粛
未来的 伝統的
女性的 男性的
希望する色
赤系、黄・オレンジ系、緑系
納品ファイル
• イラストレーター形式 (.ai)
補足説明
こちらの白地ビニール。
表面にシールとなります。
ロゴはこちらですが
オーガニックの雰囲気とは異なりますので・・
別提案いただけますと幸いです。
(フォントでも構いません!)
■ 選んだ理由

どれも素敵なので迷ったのですが、、
スタッフと一緒に決めました!

■ 提案者全員のお礼・コメント

皆様!
この度はご参加頂き誠に有難うございます。
どれも素敵で悩んだのですが、、
スタッフとともに決定させて頂きました。

今後まだまだ商品を増やす予定ですので、
その際もよろしくお願い致します。

```html
<!DOCTYPE html>
<html lang="ja">
<head>
<meta charset="utf-8">
<title>MIBAE Organic Supplement Label</title>
<link rel="stylesheet" href="https://fonts.googleapis.com/css2?family=Cinzel:wght@600&family=Cormorant+Garamond:wght@500&family=Lato:wght@400&family=Noto+Sans+JP:wght@400;500&display=swap">
<style>
  :root {
    --page: #f4f4f4;
    --label-top: #f6d4d3;
    --label-bottom: #fdf3f2;
    --heart: #f5c4c4;
    --heart-soft: rgba(246, 196, 196, 0.45);
    --ink: #2a2020;
    --brand-pink: #d98c93;
    --frame: #3a3030;
    --crown: rgba(255, 255, 255, 0.7);
  }
  * { margin: 0; padding: 0; box-sizing: border-box; }
  html, body { width: 1200px; height: 1200px; overflow: hidden; background: var(--page); }
  .label {
    position: absolute; left: 100px; top: 72px; width: 1000px; height: 1056px;
    background: linear-gradient(180deg, var(--label-top) 0%, #f9e2e1 55%, var(--label-bottom) 100%);
  }
  .label__pattern {
    position: absolute; inset: 0;
    background:
      radial-gradient(circle at 12% 22%, var(--heart-soft) 0 80px, transparent 82px),
      radial-gradient(circle at 86% 30%, var(--heart-soft) 0 90px, transparent 92px),
      radial-gradient(circle at 78% 80%, var(--heart-soft) 0 110px, transparent 112px),
      radial-gradient(circle at 20% 70%, var(--heart-soft) 0 70px, transparent 72px);
    opacity: 0.6;
  }
  .label__frame {
    position: absolute; left: 57px; top: 57px; right: 57px; bottom: 57px;
    border: 2px solid var(--frame);
  }
  .label__frame::after {
    content: ""; position: absolute; inset: 6px; border: 1px solid var(--frame);
  }
  .brand {
    position: absolute; top: 170px; width: 100%; text-align: center;
    font-family: "Cormorant Garamond", serif; font-weight: 500;
    font-size: 46px; color: var(--brand-pink); letter-spacing: 1px;
  }
  .crown {
    position: absolute; left: 380px; top: 265px; width: 240px; height: 150px;
    background: linear-gradient(180deg, var(--crown), rgba(255,255,255,0.25));
    border-radius: 60px 60px 10px 10px;
  }
  .product-name {
    position: absolute; top: 340px; width: 100%; text-align: center;
    font-family: "Cinzel", serif; font-weight: 600;
    font-size: 118px; letter-spacing: 14px; color: var(--ink); line-height: 1;
    padding-left: 14px;
  }
  .category {
    position: absolute; top: 530px; width: 100%; text-align: center;
    font-family: "Lato", sans-serif; font-weight: 400;
    font-size: 40px; letter-spacing: 7px; color: var(--ink); line-height: 74px;
  }
  .features { position: absolute; left: 0; top: 680px; width: 100%; height: 150px; }
  .feature {
    position: absolute; top: 0; width: 150px; height: 140px;
  }
  .feature svg { position: absolute; inset: 0; }
  .feature__text {
    position: absolute; top: 38px; width: 100%; text-align: center;
    font-family: "Noto Sans JP", sans-serif; font-size: 15px; line-height: 22px; color: #6a5050;
  }
  .feature--folate { left: 323px; }
  .feature--nutrients { left: 527px; }
  .features__plus {
    position: absolute; left: 480px; top: 30px; width: 40px; text-align: center;
    font-family: "Lato", sans-serif; font-size: 60px; color: var(--ink); line-height: 1;
  }
  .subtitle {
    position: absolute; top: 880px; width: 100%; text-align: center;
    font-family: "Noto Sans JP", sans-serif; font-weight: 500;
    font-size: 28px; color: var(--ink); letter-spacing: 1px;
  }
</style>
</head>
<body>
  <div class="label">
    <div class="label__pattern" role="img" aria-label="Soft pink heart pattern background"></div>
    <div class="label__frame"></div>
    <div class="brand">Florima-labo</div>
    <div class="crown" role="img" aria-label="Faint white crown ornament"></div>
    <div class="product-name">MIBAE</div>
    <div class="category">ORGANIC<br>SUPPLEMENT</div>
    <div class="features">
      <div class="feature feature--folate">
        <svg viewBox="0 0 150 140" width="150" height="140"><path d="M75 132 C30 100 5 75 5 42 C5 18 24 4 44 4 C58 4 70 12 75 24 C80 12 92 4 106 4 C126 4 145 18 145 42 C145 75 120 100 75 132 Z" fill="var(--heart)"/></svg>
        <div class="feature__text">オーガニック<br>天然葉酸</div>
      </div>
      <div class="features__plus">+</div>
      <div class="feature feature--nutrients">
        <svg viewBox="0 0 150 140" width="150" height="140"><path d="M75 132 C30 100 5 75 5 42 C5 18 24 4 44 4 C58 4 70 12 75 24 C80 12 92 4 106 4 C126 4 145 18 145 42 C145 75 120 100 75 132 Z" fill="var(--heart)"/></svg>
        <div class="feature__text">妊活必須<br>栄養素</div>
      </div>
    </div>
    <div class="subtitle">オーガニック葉酸</div>
  </div>
</body>
</html>
```